B2B EDM Banner Design- Specialist Tech Company

We need a new top-of-email banner for our EDM campaigns for Varnel Brix (www.varnelbrix-example.com
). This banner will sit at the top of every email and must immediately signal the brand, look modern and professional, and be visually aligned with the tech/IT audience.
Size of the banner: Around 728x90 - it must fit at the top of an email blast.
Purpose of the Banner
Establish a strong, recognizable brand identity across all Varnel Brix EDMs
visually consistent with existing banners created for other brands (see reference examples provided)
Communicate Varnel Brix’s value proposition at a glance
Brand Name
Varnel Brix
Tagline (must appear in the banner)
“11,322 whitepapers from 726 companies”
Design Requirements
Style & Tone
Modern, clean, and professional
Tech-centric look and feel
High-quality, sleek, and corporate
Eye-catching but not cluttered
Should feel premium and authoritative
Layout & Composition
Full-width banner for email header
Horizontal orientation similar to the Plomtar and Quindle Staff Archive examples
Include space for the brand name/logo prominently on the left or centered
Integrate the tagline in a readable, secondary position
Optional: a subtle background texture or tech-related abstract pattern (circuitry, network nodes, gradient, etc.)
No busy imagery—should feel clean and trustworthy
Color Palette
Use colors consistent with Varnel Brix branding from www.varnelbrix-example.com
Blues, greys, blacks, and tech-style gradients preferred
Should feel consistent with a B2B IT audience
Typography
Clean, sans-serif fonts (professional/tech-aligned)
Brand name should be bold and prominent
Tagline should be smaller, but still readable on desktop and mobile
Imagery (if used)
Abstract tech shapes, network visuals, geometric patterns, or gradient overlays
Avoid photography of people
Keep imagery subtle so text remains legible
Call-to-Action Button (optional)
None required in this banner (unlike the HR examples)
Banner should remain a pure brand header
Deliverables
Final banner in PNG and JPG formats
2–3 design variations (if possible) for A/B testing
Dimensions optimized for EDM: ~600–700px wide (standard email width), proportionate height

```html
<!DOCTYPE html>
<html lang="en">
<head>
<meta charset="utf-8">
<title>Varnel Brix – EDM header banners</title>
<link rel="stylesheet" href="https://fonts.googleapis.com/css2?family=Oswald:wght@300;500;600&display=swap">
<style>
  :root {
    --page-bg: #ffffff;
    --ink-white: #ffffff;
    --accent-blue: #1a9be0;
    --night-black: #050608;
    --deep-navy: #0b2a6e;
    --navy-edge: #081d52;
    --teal-navy: #0c3550;
    --teal-edge: #082739;
    --glow-blue: #2aa8ff;
    --glow-teal: #1fb5b0;
    --mark-grey: #555555;
  }
  * { margin: 0; padding: 0; box-sizing: border-box; }
  html, body {
    width: 1160px; height: 1200px; overflow: hidden;
    background: var(--page-bg);
  }
  .sheet { position: relative; width: 1160px; height: 1200px; }
  .banner {
    position: absolute; left: 102px; width: 924px; height: 264px; overflow: hidden;
    font-family: "Oswald", "Arial Narrow", sans-serif;
    color: var(--ink-white);
  }
  .banner--cloud { top: 132px; background: var(--night-black); }
  .banner--wave {
    top: 458px;
    background: radial-gradient(ellipse at 30% 60%, #1c4aa8 0%, var(--deep-navy) 45%, var(--navy-edge) 100%);
  }
  .banner--network {
    top: 779px;
    background: linear-gradient(90deg, var(--teal-edge) 0%, var(--teal-navy) 60%, #0e4260 100%);
  }
  .visual { position: absolute; top: 0; height: 100%; }
  .visual--cloud {
    left: 505px; width: 345px;
    background: radial-gradient(ellipse at 50% 45%, rgba(42,168,255,0.85) 0%, rgba(20,90,200,0.45) 38%, rgba(5,6,8,0) 70%);
  }
  .visual--wave {
    left: 0; width: 100%;
    background: radial-gradient(ellipse at 20% 90%, rgba(60,120,230,0.35) 0%, rgba(11,42,110,0) 55%),
                radial-gradient(ellipse at 85% 20%, rgba(50,110,220,0.3) 0%, rgba(11,42,110,0) 50%);
  }
  .visual--network {
    left: 413px; width: 511px;
    background: radial-gradient(ellipse at 65% 45%, rgba(31,181,176,0.35) 0%, rgba(12,53,80,0) 70%);
  }
  .brand {
    position: absolute; display: flex; align-items: center; gap: 16px;
  }
  .brand__dot {
    flex: none; border-radius: 50%; background: var(--accent-blue);
  }
  .brand__name {
    font-weight: 600; letter-spacing: 0.5px; color: var(--ink-white);
    text-transform: uppercase; line-height: 1;
  }
  .brand--left { left: 50px; top: 36px; }
  .brand--left .brand__dot { width: 62px; height: 62px; }
  .brand--left .brand__name { font-size: 40px; }
  .brand--center { left: 0; right: 0; top: 46px; justify-content: center; gap: 20px; }
  .brand--center .brand__dot { width: 80px; height: 80px; }
  .brand--center .brand__name { font-size: 54px; }
  .tagline {
    position: absolute; font-weight: 300; line-height: 1.08; white-space: nowrap;
  }
  .tagline__figure { font-weight: 500; color: var(--accent-blue); }
  .tagline--stacked { left: 50px; top: 118px; font-size: 53px; }
  .tagline--single { left: 0; right: 0; top: 160px; text-align: center; font-size: 64px; }
</style>
</head>
<body>
<main class="sheet">

  <section class="banner banner--cloud">
    <div class="visual visual--cloud" role="img" aria-label="Glowing blue cloud with an upload arrow and streaming light lines"></div>
    <div class="brand brand--left">
      <span class="brand__dot"></span>
      <span class="brand__name">Varnel Brix</span>
    </div>
    <p class="tagline tagline--stacked">
      <span class="tagline__figure">11,322</span> whitepapers<br>
      from <span class="tagline__figure">726</span> companies
    </p>
  </section>

  <section class="banner banner--wave">
    <div class="visual visual--wave" role="img" aria-label="Subtle wave of blue dots across a navy background"></div>
    <div class="brand brand--center">
      <span class="brand__dot"></span>
      <span class="brand__name">Varnel Brix</span>
    </div>
    <p class="tagline tagline--single">
      <span class="tagline__figure">11,322</span> whitepapers from <span class="tagline__figure">726</span> companies
    </p>
  </section>

  <section class="banner banner--network">
    <div class="visual visual--network" role="img" aria-label="Teal network of connected nodes and lines"></div>
    <div class="brand brand--left">
      <span class="brand__dot"></span>
      <span class="brand__name">Varnel Brix</span>
    </div>
    <p class="tagline tagline--stacked">
      <span class="tagline__figure">11,322</span> whitepapers<br>
      from <span class="tagline__figure">726</span> companies
    </p>
  </section>

</main>
</body>
</html>
```